Pig Roasting for all occasions

I am looking for a pig picture or something to get my concept going before you even start to read the details.
This design I will use for everything. T shirts, Thank You cards, etc
Perhaps something to go along with the Name. There are other
Hog Marauder picture web sites out there but I don't like any of there pictures. And for that matter I don't want to copy them any way.

My main business is Pig Roasting but I do a lot of catering along with it. I will be doing a lot of sausage (Wurst) with the pig roast
hence " Grill Fellows"
I also do beef and chicken but the main stay is Pork

Target Market(s)

For the backyard or Corporate Party - Target 50 + People

Industry/Entity Type

Catering

Contact Information for Business Card

The Hog Marauder BBQ
Pig roasting for all occasions
Grill Fellows
THEHOGMARAUDERBBQ.EXAMPLE
Dale Fenwicke
4127 Larchmont Dr
Cedar Hollow, NC 28555
(555) 273 - 6648
thehogmarauderbbq@mailbox.example

```html
<!DOCTYPE html>
<html lang="en">
<head>
<meta charset="utf-8">
<title>The Hog Marauder BBQ — Business Card</title>
<link href="https://fonts.googleapis.com/css2?family=Poiret+One&family=Libre+Baskerville:ital@1&family=Questrial&display=swap" rel="stylesheet">
<style>
  :root {
    --band: #94fff5;
    --cyan: #5cfff6;
    --ink: #5ff0ec;
    --rule: #6ff3ef;
    --faint: #eafefd;
    --faint-soft: #f8fffe;
    --paper: #ffffff;
  }
  html, body {
    margin: 0;
    padding: 0;
    overflow: hidden;
    background: var(--paper);
  }
  .card {
    position: relative;
    width: 1200px;
    height: 702px;
    overflow: hidden;
    background: var(--paper);
  }
  .card__art {
    position: absolute;
    inset: 0;
  }
  .band {
    position: absolute;
    left: 0;
    width: 100%;
    background: var(--band);
  }
  .band--top { top: 0; height: 77px; }
  .band--bottom { bottom: 0; height: 68px; }
  .headline {
    position: absolute;
    left: 0;
    width: 100%;
    top: 310px;
    margin: 0;
    text-align: center;
    font-family: "Poiret One", sans-serif;
    font-weight: 400;
    font-size: 66px;
    line-height: 1;
    letter-spacing: -0.5px;
    color: var(--ink);
    white-space: nowrap;
    transform: scaleX(0.86);
    transform-origin: 50% 50%;
  }
  .tagline {
    position: absolute;
    left: 185px;
    width: 838px;
    top: 424px;
    margin: 0;
    display: flex;
    justify-content: space-between;
    font-family: "Libre Baskerville", serif;
    font-style: italic;
    font-size: 20px;
    line-height: 1;
    color: var(--ink);
  }
  .contact {
    position: absolute;
    left: 0;
    width: 100%;
    top: 474px;
    margin: 0;
    text-align: center;
    font-family: "Questrial", sans-serif;
    font-style: normal;
    font-size: 21px;
    line-height: 28px;
    color: var(--ink);
  }
  .contact__line { display: block; white-space: nowrap; }
</style>
</head>
<body>
<main class="card">
  <svg class="card__art" width="1200" height="702" viewBox="0 0 1200 702" aria-hidden="true">
    <circle class="emblem-ring" cx="597" cy="354" r="343" fill="var(--faint-soft)" stroke="var(--faint)" stroke-width="4"/>
    <circle class="cloche-faint__knob" cx="1051" cy="418" r="35" fill="none" stroke="var(--faint)" stroke-width="9"/>
    <circle class="cloche-faint__dome" cx="1106" cy="708" r="254" fill="var(--faint)"/>
    <g class="cloche">
      <circle cx="611" cy="190" r="12" fill="none" stroke="var(--cyan)" stroke-width="3"/>
      <path d="M531 284 A80 80 0 0 1 691 284 Z" fill="var(--cyan)"/>
      <line x1="501" y1="284" x2="720" y2="284" stroke="var(--cyan)" stroke-width="3"/>
    </g>
    <line class="rule" x1="242" y1="296" x2="979" y2="296" stroke="var(--rule)" stroke-width="1.2"/>
    <line class="rule" x1="242" y1="407" x2="979" y2="407" stroke="var(--rule)" stroke-width="1.2"/>
  </svg>

  <div class="band band--top"></div>
  <div class="band band--bottom"></div>

  <h1 class="headline">Pig Roasting For All Occasions</h1>

  <p class="tagline">
    <span>The</span><span>Hog</span><span>Marauder</span><span>BBQ</span><span>Pig</span><span>roasting</span><span>for</span><span>all</span><span>occasions</span><span>Grill</span><span>Fellows</span>
  </p>

  <address class="contact">
    <span class="contact__line">THEHOGMARAUDERBBQ.EXAMPLE Dale Fenwicke 4127 Larchmont Dr Cedar Hollow, NC 28555</span>
    <span class="contact__line">(555) 273 - 6648 thehogmarauderbbq@mailbox.example</span>
  </address>
</main>
</body>
</html>
```